Email Banner for Technology Company

We need a new email banner. The purpose of the email banner is to make us look more professional as a business and keep all communications with clients uniform. The previous designs which we have included below have now become outdated as our brand has developed and we need the new banner to become more aligned and modern.

We are a marketing organization that specialises in lead generation, email newsletters are sent to prospects on a regular basis. Therefore, it is important that we have an aesthetically pleasing banner as this is the first real impression prospects have our business. First impressions matter.

We are looking for a new email banner design as the current design is now outdated and does not reflect who we are as a business.

The new banners are required for launch at the start of Q2.

There is future work in the pipeline for the winning design. We have multiple industry sites that will require the new design as well as creating each of these in multiple languages.

The design must include the Zevomarkly wording the tagline 'The Ultimate Research Library for Technology Pro's.
It needs to be creative and fun but still remain professional, sticking with the colour theme that already exists.

Requirements
Must have
• The design must include the Zevomarkly wording the tagline 'The Ultimate Research Library for Technology Pro's.

```html
<!DOCTYPE html>
<html lang="en">
<head>
<meta charset="utf-8">
<title>Zevomarkly Email Banner</title>
<link rel="stylesheet" href="https://fonts.googleapis.com/css2?family=Outfit:wght@300;400;500&display=swap">
<style>
  :root {
    --brand-blue: #00adee;
    --sky-blue: #6dcdf4;
    --ink: #000000;
    --ink-soft: rgba(0, 0, 0, 0.55);
    --paper: #ffffff;
    --paper-soft: rgba(255, 255, 255, 0.6);
  }
  * { box-sizing: border-box; margin: 0; padding: 0; }
  html, body {
    width: 1200px;
    height: 193px;
    overflow: hidden;
    background: var(--paper);
  }
  .banner {
    position: relative;
    width: 1200px;
    height: 193px;
    overflow: hidden;
    background: var(--brand-blue);
    font-family: "Outfit", sans-serif;
  }
  .banner__panel {
    position: absolute;
    inset: 0;
  }
  .decor {
    position: absolute;
  }
  .decor--upper {
    left: 70px;
    top: 0;
    width: 192px;
    height: 96px;
    border-radius: 0 0 96px 96px;
    background: radial-gradient(ellipse at 50% 10%, var(--brand-blue) 30%, var(--ink-soft) 75%, var(--brand-blue) 100%);
  }
  .decor--lower {
    left: 32px;
    top: 128px;
    width: 134px;
    height: 65px;
    border-radius: 67px 67px 0 0;
    background: radial-gradient(ellipse at 50% 100%, var(--brand-blue) 30%, var(--ink-soft) 75%, var(--brand-blue) 100%);
  }
  .decor--trail {
    left: 470px;
    top: 14px;
    width: 186px;
    height: 156px;
    border-radius: 40px;
    background: linear-gradient(145deg, var(--paper-soft), rgba(255, 255, 255, 0.15));
  }
  .brand-name {
    position: absolute;
    left: 42px;
    top: 72px;
    font-size: 38px;
    font-weight: 500;
    letter-spacing: -0.5px;
    color: var(--paper);
    line-height: 1;
  }
  .tagline {
    position: absolute;
    left: 790px;
    top: 67px;
    font-size: 24px;
    font-weight: 300;
    line-height: 32px;
    color: var(--paper);
  }
  .tagline__highlight {
    font-weight: 400;
    display: inline-block;
    border-bottom: 2px solid var(--paper);
    padding-bottom: 2px;
    line-height: 28px;
  }
  .cta {
    position: absolute;
    right: 0;
    bottom: 0;
    width: 128px;
    height: 35px;
    background: var(--paper);
    border-top-left-radius: 26px;
    color: var(--ink);
    font-size: 14px;
    font-weight: 400;
    display: flex;
    align-items: center;
    justify-content: center;
    padding-left: 8px;
    text-decoration: none;
  }
</style>
</head>
<body>
  <div class="banner">
    <svg class="banner__panel" width="1200" height="193" viewBox="0 0 1200 193" aria-hidden="true">
      <polygon class="sky-panel" points="539,0 1200,0 1200,193 717,193" fill="var(--sky-blue)"/>
    </svg>

    <div class="decor decor--upper" role="img" aria-label="Decorative concentric ring motif"></div>
    <div class="decor decor--lower" role="img" aria-label="Decorative concentric ring motif"></div>
    <div class="decor decor--trail" role="img" aria-label="Decorative trail of white dots"></div>

    <div class="brand-name">Zevomarkly</div>

    <p class="tagline">
      The Ultimate Research<br>
      Library for <span class="tagline__highlight">Technology Pro's</span>
    </p>

    <a class="cta" href="#">Click Here</a>
  </div>
</body>
</html>
```